Toronto based adult novelty shop in need of website banners for new site

We are in need of a total of seven banners for our website.  We have one of Canada's largest selections of adult novelty items and fetish wear.  We have been serving the adult online community in Canada and the world since 2008.
There are two different sizes of banners needed.  The first measures 936px x 403px and feature products.  The other three banners measure  296px x 187px and highlight our customer policies.  The overall look we are going for should convey a sense of quality and elegance and should integrate with our new theme well.  You may view the test site by visiting http://velvetmarten.ca/testshop.  The banners displayed on the test site are placeholder graphics that came with the theme (not our banners or products).  Below is the list I've compiled for the content of the banners we need.  Product descriptions for the part numbers may be viewed by using the search box on our test website (see link above).
936 x 403 banner #1: Product number B938 Raft Glide Lubricant Copy should read something like: Raft Glide Silicone, Prepare for Action! (Military theme?)
936 x 403 banner #2: Product number AC245 Brackenly Steel Locking Anal Plug Copy should read something like: Add a new dimension to anal play
936 x 403 banner #3: Product number AB545 Leather and Brocade Runa Corset Copy should read something like: Give your partner a visual feast
936 x 403 banner #4: Product number AD621 Vask Brightmoor Premium Wand Kit Copy should read something like: Electrify your partner and light them up with this exceptional all-in-one set!
296 x 187 banner #1: Return Policy
Copy should read something like: Easy Returns, Don't like it?  Send it back! (click here for more information)
296 x 187 banner #2: Free Shipping
Copy should read something like: Free Expedited Shipping on orders over $149 (click here for details)
296 x 187 banner #3: Price Matching
Copy should read something like: We'll beat any price, online or anywhere else (some conditions and exclusions apply) I believe the disclaimers in parenthesis could be replaced by asterisk if it would look better.  I will link the images to the full terms.  I hope this is enough information for you.  Please feel free to take creative liberties and let me know if anything isn't working out the way I described.
I've attached image files for the products and also a screen shot of the site in case you cannot access it.

```html
<!DOCTYPE html>
<html lang="en">
<head>
<meta charset="utf-8">
<title>Shop Home Banners</title>
<link rel="stylesheet" href="https://fonts.googleapis.com/css2?family=PT+Sans+Narrow:wght@700&family=PT+Serif&display=swap">
<style>
  :root {
    --page-bg: #f2f2f2;
    --frame: #ffffff;
    --frame-edge: #e6e6e6;
    --slate-dark: #1f232c;
    --slate-mid: #4a5060;
    --slate-tile: #2a2f3a;
    --band: #1e222b;
    --band-edge: #5a606c;
    --gold: #f2b705;
    --title-grey: #d9dadc;
    --ink: #222222;
    --tab-bg: #d9d5cf;
    --tab-edge: #a8a39b;
  }
  * { box-sizing: border-box; margin: 0; padding: 0; }
  html, body { width: 1200px; height: 576px; overflow: hidden; background: var(--page-bg); }
  body { position: relative; font-family: "PT Sans Narrow", "Arial Narrow", sans-serif; }

  .hero {
    position: absolute; left: 217px; top: 29px; width: 763px; height: 334px;
    background: var(--frame); border: 1px solid var(--frame-edge); padding: 4px 5px;
  }
  .hero-art { position: relative; width: 752px; height: 324px; overflow: hidden; background: #fff; }
  .hero-art svg { position: absolute; inset: 0; }
  .product-photo {
    position: absolute; left: 10px; top: 40px; width: 320px; height: 260px;
    background: radial-gradient(ellipse at center, #d4d6d9 0%, #eef0f1 55%, #ffffff 80%);
  }
  .hero-title-band {
    position: absolute; left: 376px; top: 29px; width: 376px; height: 51px;
    background: rgba(22, 25, 32, 0.55);
  }
  .hero-title {
    position: absolute; right: 24px; top: 34px;
    font-size: 37px; line-height: 40px; color: var(--title-grey); letter-spacing: 0.2px;
  }
  .hero-tagline {
    position: absolute; left: 418px; width: 290px; top: 160px; text-align: center;
    font-size: 35px; line-height: 42px; color: var(--gold);
    text-shadow: 2px 3px 4px rgba(0,0,0,0.7); letter-spacing: -0.3px;
  }

  .policy {
    position: absolute; top: 371px; width: 249px; height: 161px;
    background: var(--frame); border: 1px solid var(--frame-edge); padding: 4px 5px;
  }
  .policy-returns { left: 217px; }
  .policy-price { left: 473px; }
  .policy-shipping { left: 730px; }
  .policy-tile {
    position: relative; width: 100%; height: 152px; background: var(--slate-tile);
  }
  .policy-band {
    position: absolute; left: 2px; right: 4px; top: 28px; height: 90px;
    background: var(--band); border-left: 4px solid var(--band-edge);
    display: flex; align-items: center; justify-content: center;
  }
  .policy-copy {
    color: #fff; text-align: center; font-size: 25px; line-height: 22px;
    text-transform: uppercase; letter-spacing: -0.3px;
    text-shadow: 1px 2px 3px rgba(0,0,0,0.6);
  }
  .read-more {
    position: absolute; left: 50%; transform: translateX(-50%); top: 127px;
    width: 84px; height: 19px; background: var(--gold); border-radius: 2px;
    font-size: 12px; line-height: 19px; text-align: center; color: #111;
  }

  .featured {
    position: absolute; left: 215px; top: 550px; width: 763px; height: 40px;
    background: var(--frame); padding: 10px 16px;
  }
  .featured h2 {
    font-family: "PT Serif", Georgia, serif; font-weight: 400; font-size: 12.5px;
    color: var(--ink); letter-spacing: 0.3px;
  }

  .reviews-tab {
    position: absolute; left: 1167px; top: 252px; width: 36px; height: 105px;
    background: var(--tab-bg); border: 1px solid var(--tab-edge); border-radius: 4px 0 0 4px;
    box-shadow: -1px 1px 3px rgba(0,0,0,0.2);
    display: flex; align-items: center; justify-content: center;
  }
  .reviews-tab span {
    writing-mode: vertical-rl; font-family: Arial, sans-serif; font-weight: 400;
    font-size: 11px; letter-spacing: 0.5px; color: #444;
  }
</style>
</head>
<body>
  <section class="hero">
    <div class="hero-art">
      <div class="product-photo" role="img" aria-label="Product photo: two polished steel locking anal plugs, one opened with a padlock, one closed"></div>
      <svg width="752" height="324" viewBox="0 0 752 324" aria-hidden="true">
        <defs>
          <radialGradient id="slateGlow" cx="0.6" cy="0.55" r="0.6">
            <stop offset="0" stop-color="#525a6a"/>
            <stop offset="1" stop-color="#1f232c"/>
          </radialGradient>
        </defs>
        <path d="M346 0 C 382 105, 376 225, 328 324 L752 324 L752 0 Z" fill="url(#slateGlow)"/>
      </svg>
      <div class="hero-title-band"></div>
      <h1 class="hero-title">The Steel Anal Lock</h1>
      <p class="hero-tagline">Add a new dimension to anal play!</p>
    </div>
  </section>

  <a class="policy policy-returns">
    <div class="policy-tile">
      <div class="policy-band"><p class="policy-copy">Easy returns!<br>Don't like it?<br>Send it back!</p></div>
      <span class="read-more">READ MORE</span>
    </div>
  </a>
  <a class="policy policy-price">
    <div class="policy-tile">
      <div class="policy-band"><p class="policy-copy">We'll beat any<br>price, online or<br>anywhere else!</p></div>
      <span class="read-more">READ MORE</span>
    </div>
  </a>
  <a class="policy policy-shipping">
    <div class="policy-tile">
      <div class="policy-band"><p class="policy-copy">Free expedited<br>shipping on<br>orders over $149</p></div>
      <span class="read-more">READ MORE</span>
    </div>
  </a>

  <section class="featured"><h2>FEATURED PRODUCTS</h2></section>

  <aside class="reviews-tab"><span>★ REVIEWS</span></aside>
</body>
</html>
```